Lantern Motion for Neighbors Business Cards

I need business cards for staff in a new startup. Our company name is Movrela - we train Tai Chi teachers. But our biggest project is called Lantern Motion for Neighbors - a federal project to put together free Tai Chi classes for Vets all across America. It's a young company, with a spirit of excitement, passion, a desire to do good for others (our Vets) and a modern style and sensibility. In other words, not old-fashioned Asian martial arts theme, but something new.

Industry/Entity Type

Health And Wellness

Contact Information for Business Card

The topic is ancient healing, but the company is the Pembrooks - so I'd like a card design that captures that.

Font styles to use
Sans Serif

Colors

Designer to choose colors to be used in the design.

Requirements
Nice to have
• I've got two logos - one for the company and one for the project. I want to see if we can incorporate them both without it becoming too busy.
Should not have
• Overly old-fashioned yin-yang themes.

```html
<!DOCTYPE html>
<html lang="en">
<head>
<meta charset="utf-8">
<title>Lantern Motion for Neighbors — Business Cards</title>
<link href="https://fonts.googleapis.com/css2?family=Open+Sans:wght@400;600&family=Josefin+Sans:wght@300;400&family=Tinos:wght@700&display=swap" rel="stylesheet">
<style>
  :root {
    --stage: #5a5a5a;
    --card: #111111;
    --card-edge: #1a1a1a;
    --shadow-figure: #242424;
    --gold: #b98f5e;
    --red: #e01a22;
    --white: #f2f2f2;
  }
  * { box-sizing: border-box; margin: 0; padding: 0; }
  html, body { width: 1200px; height: 1021px; overflow: hidden; }
  body {
    background: var(--stage);
    display: flex;
    flex-direction: column;
    align-items: center;
    justify-content: center;
    gap: 60px;
    font-family: "Open Sans", sans-serif;
  }
  .card {
    position: relative;
    width: 700px;
    height: 400px;
    background: var(--card);
    box-shadow: 0 18px 40px rgba(0,0,0,0.45);
    overflow: hidden;
  }

  /* Front */
  .figure {
    position: absolute;
    background: linear-gradient(180deg, var(--shadow-figure), var(--card-edge));
    border-radius: 40px 40px 12px 12px;
    opacity: 0.9;
  }
  .figure--left { left: 40px; top: 70px; width: 150px; height: 230px; }
  .figure--right { right: 40px; top: 150px; width: 170px; height: 230px; }
  .project-mark {
    position: absolute;
    left: 170px; top: 140px;
    display: flex; align-items: center; gap: 26px;
  }
  .project-mark__ring {
    width: 120px; height: 120px;
    border: 3px solid var(--gold);
    border-radius: 50%;
    flex: none;
  }
  .project-mark__name {
    font-family: "Josefin Sans", sans-serif;
    font-weight: 300;
    color: var(--gold);
    line-height: 1;
  }
  .project-mark__name .line1 { display: block; font-size: 40px; letter-spacing: 1px; }
  .project-mark__name .line2 { display: block; font-size: 17px; letter-spacing: 5px; margin-top: 6px; }

  /* Back */
  .person { position: absolute; left: 60px; top: 80px; }
  .person__name {
    font-family: "Tinos", sans-serif;
    font-weight: 700;
    font-size: 25px;
    color: var(--red);
  }
  .person__role { font-size: 17px; color: var(--white); margin-top: -2px; }
  .contact {
    position: absolute; left: 60px; top: 185px;
    color: var(--white); font-size: 17px; line-height: 1.35;
    list-style: none;
  }
  .contact li { display: flex; align-items: center; gap: 8px; }
  .contact .address { display: block; margin-bottom: 8px; }
  .contact svg { width: 15px; height: 15px; flex: none; }
  .company-mark {
    position: absolute; right: 70px; top: 130px;
    display: flex; align-items: center; gap: 16px;
  }
  .company-mark__dot {
    width: 110px; height: 110px; border-radius: 50%;
    background: var(--red);
  }
  .company-mark__name {
    font-size: 34px; font-weight: 600; color: var(--red);
  }
  .social {
    position: absolute; right: 70px; bottom: 40px;
    display: flex; gap: 12px; list-style: none;
  }
  .social li {
    width: 30px; height: 30px; border-radius: 50%;
    background: var(--red);
  }
</style>
</head>
<body>
  <section class="card card--front">
    <div class="figure figure--left" role="img" aria-label="Faint silhouette of a tai chi practitioner"></div>
    <div class="figure figure--right" role="img" aria-label="Faint silhouette of a tai chi practitioner"></div>
    <div class="project-mark">
      <div class="project-mark__ring"></div>
      <p class="project-mark__name">
        <span class="line1">LANTERN MOTION</span>
        <span class="line2">FOR NEIGHBORS</span>
      </p>
    </div>
  </section>

  <section class="card card--back">
    <div class="person">
      <h1 class="person__name">Marcus Ellery-Hale</h1>
      <p class="person__role">Founder</p>
    </div>
    <ul class="contact">
      <li class="address">2180 Orchard Ave. Ste. 214<br>Seabright, CA 90412</li>
      <li>
        <svg viewBox="0 0 16 16"><path fill="#e01a22" d="M3.5 1l2.5 3-1.5 1.6c.8 2 2.4 3.6 4.4 4.4L10.5 8.5l3 2.5-1.3 2.6C7 13.3 2.7 9 2.4 3.8z"/></svg>
        555-214-0187
      </li>
      <li>
        <svg viewBox="0 0 16 16"><rect x="1.5" y="3.5" width="13" height="9" fill="none" stroke="#e01a22" stroke-width="1.4"/><path d="M1.5 3.5l6.5 5 6.5-5" fill="none" stroke="#e01a22" stroke-width="1.4"/></svg>
        info@movrela.net
      </li>
      <li>
        <svg viewBox="0 0 16 16"><circle cx="8" cy="8" r="6.3" fill="none" stroke="#e01a22" stroke-width="1.4"/><path d="M1.7 8h12.6M8 1.7c-3 3.5-3 9 0 12.6M8 1.7c3 3.5 3 9 0 12.6" fill="none" stroke="#e01a22" stroke-width="1.2"/></svg>
        www.movrela.net
      </li>
    </ul>
    <div class="company-mark">
      <div class="company-mark__dot"></div>
      <span class="company-mark__name">Movrela</span>
    </div>
    <ul class="social" aria-label="Social profiles">
      <li></li><li></li><li></li><li></li>
    </ul>
  </section>
</body>
</html>
```